Upmarket building and construction company needs signage

Our building company R Brent Construction, needs signage to put up on the side of our vehicle trailers and on site fencing. We are a building company that specialises in residential construction and carpentry .

I will attach our logo and some inspirational pics for site fencing as well as what our trailer looks like .
Other details i would like on the sign are our
( email) rbrentconstruction@mailbox-example.net
(mobile ) 0493 518 264
(website ) rbrentconstruction. example.net

Target Market(s)

Home owners looking for a reliable local builder who produces good quality work. I have attached some inspirational pics.

Industry/Entity Type

Building and Construction

Colors

Designer to choose colors to be used in the design.

Requirements
Must have
• Our logo, contact information
Nice to have
• We would like the design to have elements of being Elegant, Serious, Modern, Professional, Masculine, Conservative and Upmarket.

```html
<!DOCTYPE html>
<html lang="en">
<head>
<meta charset="utf-8">
<title>R Brent Construction – Trailer Sign</title>
<link rel="stylesheet" href="https://fonts.googleapis.com/css2?family=Archivo:wdth,wght@62..125,400..800&display=swap">
<style>
  :root {
    --page: #ffffff;
    --panel: #e2e2e2;
    --forest: #17473f;
    --ink: #1d1d1d;
    --rule: #2a2a2a;
    --photo-light: #d9dbda;
    --photo-mid: #9aa6a2;
  }
  * { margin: 0; padding: 0; box-sizing: border-box; }
  html, body {
    width: 969px; height: 1200px; overflow: hidden;
    background: var(--page);
    font-family: "Archivo", Arial, sans-serif;
  }
  .canvas { position: relative; width: 969px; height: 1200px; }
  .sign {
    position: absolute; left: 44px; top: 380px;
    width: 880px; height: 440px;
    background: var(--panel);
    box-shadow: 0 18px 40px rgba(0,0,0,0.18);
    overflow: hidden;
  }
  .sign__photo {
    position: absolute; left: 0; top: 0;
    width: 350px; height: 100%;
    background:
      linear-gradient(90deg, rgba(226,226,226,0) 55%, var(--panel) 100%),
      repeating-linear-gradient(180deg, var(--forest) 0 34px, var(--photo-light) 34px 70px),
      linear-gradient(90deg, var(--photo-mid), var(--photo-light));
    background-blend-mode: normal, multiply, normal;
  }
  .sign__headline {
    position: absolute; left: 412px; top: 54px;
    color: var(--forest);
    font-weight: 800; font-stretch: 125%;
    font-size: 55px; line-height: 0.98; letter-spacing: -1.5px;
  }
  .contact {
    position: absolute; left: 310px; top: 330px;
    width: 500px;
  }
  .contact__rule-top {
    position: absolute; left: 0; top: 0; width: 435px;
    border-top: 1px solid var(--rule);
  }
  .contact__rule-bottom {
    position: absolute; left: 0; top: 75px; width: 375px;
    border-top: 1px solid var(--rule);
  }
  .contact__list { list-style: none; position: absolute; left: 0; top: 10px; }
  .contact__item {
    display: flex; align-items: center; gap: 7px;
    height: 21px;
    color: var(--forest);
    font-weight: 700; font-stretch: 125%; font-size: 12.5px;
  }
  .contact__icon { width: 12px; height: 12px; flex: none; }
  .brand {
    position: absolute; right: 44px; top: 358px;
    color: var(--ink);
    font-weight: 400; font-stretch: 100%;
    font-size: 20px; line-height: 1.05; letter-spacing: 1px;
    text-transform: uppercase; text-align: left;
  }
</style>
</head>
<body>
<main class="canvas">
  <section class="sign">
    <div class="sign__photo" role="img" aria-label="Photograph of a modern apartment tower with curved white balconies and dark green balcony undersides"></div>

    <h1 class="sign__headline">Built with<br>Purpose,<br>Designed<br>for Life.</h1>

    <div class="contact">
      <div class="contact__rule-top"></div>
      <ul class="contact__list">
        <li class="contact__item">
          <svg class="contact__icon" viewBox="0 0 12 12" fill="none" stroke="currentColor" stroke-width="1.2"><rect x="3" y="0.8" width="6" height="10.4" rx="1.2"/><line x1="5.2" y1="9.4" x2="6.8" y2="9.4"/></svg>
          rbrentconstruction@mailbox-example.net
        </li>
        <li class="contact__item">
          <svg class="contact__icon" viewBox="0 0 12 12" fill="none" stroke="currentColor" stroke-width="1.2"><rect x="0.8" y="2.2" width="10.4" height="7.6" rx="1"/><polyline points="1,2.6 6,6.6 11,2.6"/></svg>
          0493 518 264
        </li>
        <li class="contact__item">
          <svg class="contact__icon" viewBox="0 0 12 12" fill="none" stroke="currentColor" stroke-width="1.1"><circle cx="6" cy="6" r="5.2"/><ellipse cx="6" cy="6" rx="2.3" ry="5.2"/><line x1="0.8" y1="6" x2="11.2" y2="6"/><line x1="1.6" y1="3.3" x2="10.4" y2="3.3"/><line x1="1.6" y1="8.7" x2="10.4" y2="8.7"/></svg>
          rbrentconstruction. example.net
        </li>
      </ul>
      <div class="contact__rule-bottom"></div>
    </div>

    <p class="brand">R Brent<br>Construction</p>
  </section>
</main>
</body>
</html>
```